Dual (Twin) Wet Wipe Packaging

We are a NY Based Hygiene Brand Specifically for couples, Creating Dual products for Him and Her,
Brand Name is plimora.
Our Initial Product is a single Wet wipe Dual Package with perforated lines one wipe for him and one for her used for after sex.
We Would like to see designs that show a bold modern design with slight edgy to bring out the fun!
The final design Should bring out the idea of couples, connection and bond,

Attached Are photos of color ideas And Attached Design ideas.

The measurement of each half should be 7*9 cm total 14*9 cm with both attached.

```html
<!DOCTYPE html>
<html lang="en">
<head>
<meta charset="utf-8">
<title>plimora Intimate Wet Wipes – Dual Pack</title>
<link href="https://fonts.googleapis.com/css2?family=Montserrat:wght@400;900&family=Roboto+Condensed:wght@400;700&display=swap" rel="stylesheet">
<style>
  :root {
    --page-bg: #dedede;
    --him-top: #0cb6e6;
    --him-bottom: #175fb8;
    --him-band: #0a3670;
    --him-accent: #1ec4f2;
    --him-tag: #1a8fd6;
    --her-top: #ee46b0;
    --her-bottom: #b3227f;
    --her-band: #4a0837;
    --her-accent: #ff38cc;
    --her-tag: #e0319f;
    --white: #ffffff;
    --tag-bg: #f4f4f6;
    --condensed: "Roboto Condensed", "Arial Narrow", sans-serif;
    --display: "Montserrat", Arial, sans-serif;
  }
  * { box-sizing: border-box; margin: 0; padding: 0; }
  html, body { width: 1200px; height: 960px; overflow: hidden; }
  body { background: var(--page-bg); position: relative; }

  .dual-pack {
    position: absolute; left: 135px; top: 155px;
    width: 930px; height: 650px;
    display: flex; border-radius: 8px; overflow: hidden;
  }
  .sachet { position: relative; width: 465px; height: 650px; color: var(--white); }
  .sachet--him { background: linear-gradient(180deg, var(--him-top) 0%, #1aa6e0 45%, var(--him-bottom) 100%); --accent: var(--him-accent); --band: var(--him-band); --tag: var(--him-tag); }
  .sachet--her { background: linear-gradient(180deg, var(--her-top) 0%, #dc3aa2 45%, var(--her-bottom) 100%); --accent: var(--her-accent); --band: var(--her-band); --tag: var(--her-tag); }

  .brand {
    position: absolute; left: 52px; top: 84px;
    display: flex; align-items: center; gap: 10px;
    font-family: var(--condensed); font-weight: 700; font-size: 44px; color: var(--white);
    letter-spacing: 0.5px;
  }
  .brand__dot { width: 22px; height: 22px; border-radius: 50%; background: var(--white); }

  .variant-tag {
    position: absolute; right: 0; top: 86px;
    width: 151px; height: 41px;
    background: var(--tag-bg); border-radius: 21px 0 0 21px;
    display: flex; align-items: center; gap: 10px; padding-left: 14px;
    font-family: var(--condensed); font-weight: 700; font-size: 25px; color: var(--tag);
    letter-spacing: 0.5px;
  }
  .variant-tag svg { width: 24px; height: 26px; }

  .couple-art {
    position: absolute; left: 204px; top: 117px; width: 220px; height: 363px;
    border-radius: 40px;
  }
  .sachet--him .couple-art { background: linear-gradient(160deg, rgba(10,60,130,0.18), rgba(10,60,130,0.05)); }
  .sachet--her .couple-art { background: linear-gradient(160deg, rgba(110,10,80,0.18), rgba(110,10,80,0.05)); }

  .headline { position: absolute; left: 52px; top: 346px; }
  .headline__main { font-family: var(--display); font-weight: 900; font-size: 54px; line-height: 1; letter-spacing: 1px; }
  .headline__sub { font-family: var(--display); font-weight: 400; font-size: 45px; line-height: 1; margin-top: 10px; letter-spacing: 1px; }

  .tagline { position: absolute; left: 52px; top: 455px; font-family: var(--condensed); font-size: 22px; }
  .claim { position: absolute; left: 52px; top: 486px; font-family: var(--condensed); font-size: 18px; color: var(--accent); }

  .benefits {
    position: absolute; left: 0; bottom: 0; width: 100%; height: 120px;
    background: var(--band);
    display: flex; align-items: flex-start; padding: 20px 0 0 50px; gap: 0;
  }
  .benefit { display: flex; align-items: center; gap: 8px; font-family: var(--condensed); font-size: 15.5px; line-height: 1.1; }
  .benefit svg { width: 32px; height: 34px; flex: none; }
  .benefit:nth-child(1) { width: 135px; }
  .benefit:nth-child(2) { width: 96px; }
</style>
</head>
<body>
<main class="dual-pack">
  <section class="sachet sachet--him">
    <div class="brand"><span class="brand__dot"></span>plimora</div>
    <div class="variant-tag">
      <svg viewBox="0 0 24 26" fill="none" stroke="currentColor" stroke-width="2.4" stroke-linecap="round"><circle cx="10" cy="10" r="7"/><path d="M15 15l6 6M21 15v6h-6"/></svg>
      FOR HIM
    </div>
    <div class="couple-art" role="img" aria-label="Single-line drawing of a man's figure"></div>
    <div class="headline">
      <div class="headline__main">INTIMATE</div>
      <div class="headline__sub">WET WIPES</div>
    </div>
    <p class="tagline">Clean Intimate Areas After Sex</p>
    <p class="claim">Kill Germs &amp; Relive Ordor</p>
    <div class="benefits">
      <div class="benefit">
        <svg viewBox="0 0 32 34" fill="none" stroke="var(--accent)" stroke-width="1.6" stroke-linejoin="round"><path d="M11 2l2 7 7 2-7 2-2 7-2-7-7-2 7-2z"/><path d="M26 13l1 3 3 1-3 1-1 3-1-3-3-1 3-1z"/><path d="M17 22l1 4 4 1-4 1-1 4-1-4-4-1 4-1z"/></svg>
        <span>Easy &amp; Gentle<br>Cleaning</span>
      </div>
      <div class="benefit">
        <svg viewBox="0 0 32 34" fill="none" stroke="var(--accent)" stroke-width="1.6" stroke-linecap="round"><path d="M4 31C8 20 16 10 29 4c0 10-6 20-18 22"/><path d="M4 31L22 11M10 20h8M14 15h9"/></svg>
        <span>Safe for<br>Skin</span>
      </div>
      <div class="benefit">
        <svg viewBox="0 0 32 34" fill="none" stroke="var(--accent)" stroke-width="1.6" stroke-linecap="round"><path d="M9 13a8 8 0 0 1 14 0"/><path d="M21 9l2 4 4-2"/><path d="M26 18a8 8 0 0 1-5 11"/><path d="M6 18a8 8 0 0 0 6 11"/><circle cx="9" cy="24" r="3"/><circle cx="23" cy="24" r="3"/></svg>
        <span>Natural &amp;<br>Biodegradable</span>
      </div>
    </div>
  </section>

  <section class="sachet sachet--her">
    <div class="brand"><span class="brand__dot"></span>plimora</div>
    <div class="variant-tag">
      <svg viewBox="0 0 24 26" fill="none" stroke="currentColor" stroke-width="2.4" stroke-linecap="round"><circle cx="12" cy="9" r="7"/><path d="M12 16v9M8 21h8"/></svg>
      FOR HER
    </div>
    <div class="couple-art" role="img" aria-label="Single-line drawing of a woman's figure"></div>
    <div class="headline">
      <div class="headline__main">INTIMATE</div>
      <div class="headline__sub">WET WIPES</div>
    </div>
    <p class="tagline">Clean Intimate Areas After Sex</p>
    <p class="claim">Kill Germs &amp; Relive Ordor</p>
    <div class="benefits">
      <div class="benefit">
        <svg viewBox="0 0 32 34" fill="none" stroke="var(--accent)" stroke-width="1.6" stroke-linejoin="round"><path d="M11 2l2 7 7 2-7 2-2 7-2-7-7-2 7-2z"/><path d="M26 13l1 3 3 1-3 1-1 3-1-3-3-1 3-1z"/><path d="M17 22l1 4 4 1-4 1-1 4-1-4-4-1 4-1z"/></svg>
        <span>Easy &amp; Gentle<br>Cleaning</span>
      </div>
      <div class="benefit">
        <svg viewBox="0 0 32 34" fill="none" stroke="var(--accent)" stroke-width="1.6" stroke-linecap="round"><path d="M4 31C8 20 16 10 29 4c0 10-6 20-18 22"/><path d="M4 31L22 11M10 20h8M14 15h9"/></svg>
        <span>Safe for<br>Skin</span>
      </div>
      <div class="benefit">
        <svg viewBox="0 0 32 34" fill="none" stroke="var(--accent)" stroke-width="1.6" stroke-linecap="round"><path d="M9 13a8 8 0 0 1 14 0"/><path d="M21 9l2 4 4-2"/><path d="M26 18a8 8 0 0 1-5 11"/><path d="M6 18a8 8 0 0 0 6 11"/><circle cx="9" cy="24" r="3"/><circle cx="23" cy="24" r="3"/></svg>
        <span>Natural &amp;<br>Biodegradable</span>
      </div>
    </div>
  </section>
</main>
</body>
</html>
```